Flyer für KFZ-Gutachter
Zielgruppe
NFZ und KFZ Gutachten. Firma ist neu gegründet und Flyer wird benötigt um sich bei Werkstätten, Versicherungen und Privatkunden vorzustellen.
Aufgabenstellung
Es soll elegant, klassisch sein und angelehnt sein an meine Website https://www.holvarentis.de/ Handynummer 0157 - 62830417 bitte einpflegen. Außerdem sollten die Logos des Bundesverbandes und der Zertifizierung mit im Flyer eingebunden werden. Diese lade ich hoch. Auch das korrekte Logo lade ich hoch.

```html
<!DOCTYPE html>
<html lang="de">
<head>
<meta charset="utf-8">
<title>Holvarentis – Flyer</title>
<link href="https://fonts.googleapis.com/css2?family=Source+Serif+4:wght@400;600&display=swap" rel="stylesheet">
<style>
  :root {
    --ink: #171717;
    --paper: #f1f1f1;
    --grey: #d4d4d4;
    --white: #ffffff;
    --text-dark: #2a2a2a;
    --text-muted: #555555;
    --photo-top: #5a5e62;
    --photo-bottom: #1c1d1f;
    --backdrop: #f3f3f2;
  }
  html, body {
    margin: 0;
    width: 1080px;
    height: 1200px;
    overflow: hidden;
    background: var(--backdrop);
    font-family: "Source Serif 4", Georgia, serif;
  }
  .flyer {
    position: absolute;
    left: 128px;
    top: 17px;
    width: 824px;
    height: 1166px;
    background: var(--grey);
    overflow: hidden;
  }
  .hero-shape { position: absolute; left: 0; top: 0; }
  .brand-box {
    position: absolute;
    left: 251px; top: 0;
    width: 330px; height: 285px;
    background: var(--ink);
    display: flex;
    flex-direction: column;
    align-items: center;
    justify-content: center;
    gap: 18px;
  }
  .brand-mark { width: 22px; height: 22px; background: var(--white); }
  .brand-name {
    color: var(--white);
    font-size: 40px;
    font-weight: 600;
    letter-spacing: 2px;
    text-transform: uppercase;
  }
  .headline {
    position: absolute;
    left: 0; right: 0; top: 418px;
    margin: 0;
    text-align: center;
    color: var(--white);
    font-weight: 400;
    font-size: 53px;
    letter-spacing: -0.5px;
  }
  .headline-rule {
    position: absolute;
    left: 482px; top: 503px;
    width: 244px; height: 2px;
    background: var(--white);
  }
  .subline {
    position: absolute;
    right: 98px; top: 542px;
    margin: 0;
    text-align: right;
    color: var(--white);
    font-size: 25px;
    line-height: 31px;
    font-weight: 400;
  }
  .service-card {
    position: absolute;
    background: var(--paper);
    box-sizing: border-box;
    padding: 44px 16px 0;
    text-align: center;
    color: var(--text-dark);
  }
  .service-card.accident { left: 106px; top: 673px; width: 187px; height: 298px; }
  .service-card.value { left: 318px; top: 656px; width: 190px; height: 333px; padding-top: 61px; }
  .service-card.damage { left: 537px; top: 673px; width: 187px; height: 298px; }
  .service-icon { width: 48px; height: 40px; display: block; margin: 0 auto; }
  .service-title { margin: 24px 0 0; font-size: 16px; font-weight: 600; }
  .service-rule { width: 42px; height: 1px; background: var(--text-dark); margin: 12px auto 14px; }
  .service-text { margin: 0; font-size: 11px; line-height: 13px; color: var(--text-muted); text-align: left; }
  .footer {
    position: absolute;
    left: 0; top: 951px;
    width: 824px; height: 215px;
    background: var(--ink);
  }
  .phone-box {
    position: absolute;
    left: 59px; top: 63px;
    width: 277px; height: 53px;
    background: var(--white);
    display: flex;
    align-items: center;
    gap: 16px;
    padding-left: 20px;
    box-sizing: border-box;
    font-size: 29px;
    color: var(--ink);
    letter-spacing: -0.5px;
  }
  .address {
    position: absolute;
    left: 59px; top: 130px;
    margin: 0;
    color: #e6e6e6;
    font-size: 21px;
  }
  .web {
    position: absolute;
    left: 61px; top: 163px;
    margin: 0;
    color: #cfcfcf;
    font-size: 13px;
    letter-spacing: 9px;
    text-transform: uppercase;
  }
  .cert-strip {
    position: absolute;
    left: 486px; top: 83px;
    width: 338px; height: 75px;
    background: var(--white);
    display: flex;
    align-items: center;
    gap: 18px;
    padding-left: 36px;
    box-sizing: border-box;
  }
  .badge-round { width: 44px; height: 44px; border-radius: 50%; background: #3e6d94; }
  .badge-oval { width: 66px; height: 44px; border-radius: 50%; background: #8fa3b8; }
  .expert {
    border-left: 3px solid #c0392b;
    padding-left: 10px;
    color: var(--ink);
  }
  .expert-name { font-size: 12px; margin: 0; }
  .expert-role { font-size: 6px; line-height: 7px; margin: 2px 0 0; width: 90px; color: var(--text-muted); }
</style>
</head>
<body>
  <main class="flyer">
    <svg class="hero-shape" width="824" height="760" viewBox="0 0 824 760">
      <defs>
        <linearGradient id="heroTone" x1="0" y1="0" x2="1" y2="1">
          <stop offset="0" stop-color="var(--photo-top)"/>
          <stop offset="1" stop-color="var(--photo-bottom)"/>
        </linearGradient>
      </defs>
      <polygon role="img" aria-label="Foto: Kfz-Sachverständiger prüft ein Fahrzeug in der Werkstatt" points="0,132 824,77 824,667 0,723" fill="url(#heroTone)"/>
    </svg>

    <div class="brand-box">
      <span class="brand-mark"></span>
      <span class="brand-name">Holvarentis</span>
    </div>

    <h1 class="headline">Ihr Experte für Gutachten</h1>
    <div class="headline-rule"></div>
    <p class="subline">Präzise Bewertungen<br>für Ihre Bedürfnisse</p>

    <section class="service-card accident">
      <svg class="service-icon" viewBox="0 0 48 40">
        <polygon points="16,2 19,9 26,6 22,13 28,16 20,17 18,24 14,18 8,20 11,13 5,9 13,9" fill="#171717"/>
        <path d="M4 26 L10 22 L20 22 L22 30 L22 36 L4 36 Z" fill="#171717"/>
        <path d="M26 24 L30 18 L42 18 L46 26 L46 36 L26 36 Z" fill="#171717"/>
        <rect x="31" y="21" width="10" height="5" fill="#f1f1f1"/>
        <circle cx="30" cy="37" r="3" fill="#f1f1f1" stroke="#171717" stroke-width="2"/>
        <circle cx="42" cy="37" r="3" fill="#f1f1f1" stroke="#171717" stroke-width="2"/>
      </svg>
      <h2 class="service-title">Unfallgutachten</h2>
      <div class="service-rule"></div>
      <p class="service-text">Wir erstellen detaillierte Unfall­gutachten, die Ihnen bei der Schadensregulierung helfen und für Versicherungen präzise nachvollziehbar sind.</p>
    </section>

    <section class="service-card value">
      <svg class="service-icon" viewBox="0 0 48 40">
        <path d="M8 20 L13 8 L35 8 L40 20 L42 22 L42 34 L6 34 L6 22 Z" fill="#171717"/>
        <path d="M15 11 L33 11 L36 19 L12 19 Z" fill="#f1f1f1"/>
        <circle cx="13" cy="26" r="2.5" fill="#f1f1f1"/>
        <circle cx="35" cy="26" r="2.5" fill="#f1f1f1"/>
        <rect x="8" y="34" width="7" height="4" fill="#171717"/>
        <rect x="33" y="34" width="7" height="4" fill="#171717"/>
      </svg>
      <h2 class="service-title">Wertgutachten</h2>
      <div class="service-rule"></div>
      <p class="service-text">Erhalten Sie fundierte Wertgut­achten, die Ihnen bei Kaufent­scheidungen oder bei der Schadenregulierung nützlich sein können.</p>
    </section>

    <section class="service-card damage">
      <svg class="service-icon" viewBox="0 0 48 40">
        <g stroke="#171717" stroke-width="2" stroke-linecap="round">
          <line x1="6" y1="4" x2="14" y2="10"/>
          <line x1="4" y1="10" x2="12" y2="15"/>
          <line x1="12" y1="2" x2="18" y2="8"/>
        </g>
        <path d="M18 24 L22 18 L38 18 L42 24 L42 36 L18 36 Z" fill="#171717"/>
        <rect x="24" y="20" width="12" height="4" fill="#f1f1f1"/>
        <circle cx="24" cy="29" r="2" fill="#f1f1f1"/>
      </svg>
      <h2 class="service-title">Schadensgutachten</h2>
      <div class="service-rule"></div>
      <p class="service-text">Präzise Schadensgutachten, die alle relevanten Informationen enthalten und die rechtlichen Anforderungen erfüllen.</p>
    </section>

    <footer class="footer">
      <div class="phone-box">
        <svg width="22" height="22" viewBox="0 0 24 24" aria-hidden="true">
          <path d="M6.6 10.8a15.1 15.1 0 0 0 6.6 6.6l2.2-2.2a1 1 0 0 1 1-.25 11.4 11.4 0 0 0 3.6.57 1 1 0 0 1 1 1V20a1 1 0 0 1-1 1A17 17 0 0 1 3 4a1 1 0 0 1 1-1h3.5a1 1 0 0 1 1 1c0 1.25.2 2.45.57 3.57a1 1 0 0 1-.25 1z" fill="#171717"/>
        </svg>
        <span>0157 628 304 17</span>
      </div>
      <p class="address">Lindenweg 12 — 70839 Kornstadt</p>
      <p class="web">www.holvarentis.de</p>
      <div class="cert-strip">
        <span class="badge-round" role="img" aria-label="Zertifizierungssiegel"></span>
        <span class="badge-oval" role="img" aria-label="Siegel des Bundesverbandes"></span>
        <div class="expert">
          <p class="expert-name">Jonas Merkwald</p>
          <p class="expert-role">Geprüfter Sachverständiger für Fahrzeugschäden und Fahrzeugbewertung</p>
        </div>
      </div>
    </footer>
  </main>
</body>
</html>
```